Yoga for Scoliosis business card/logo design

I need a business card/logo design for my new business. I am a registered yoga teacher and am certified in yoga for scoliosis. I'd like my card to read "Marlow Yoga Yoga for a Healthy Spine" and would like to incorporate one of the letters in my name{ ie the first vertical line of the letter " H "or "D"} to resemble a scoliotic spine. I regularly teach the following:Yoga for Scoliosis, Yoga for Back Health, Hatha yoga, Vinyasa yoga with Iyengar style alignment. This business is mostly for private clients, but I also teach group, semi-private & work shop classes. I like the colors green (light emerald) and royal blue. I'd like the design to be somewhat sleek, but not too modern. I also like the idea of a ying/yang symbol with a scoliotic spine dviding it.

Danielle Marlow
200 RYT, Certified Yoga for Scoliosis Instructor
MarlowYoga.example
MarlowYoga@mailbox.example
555-412-3097

```html
<!DOCTYPE html>
<html lang="en">
<head>
<meta charset="utf-8">
<title>Marlow Yoga – Business Card</title>
<link rel="stylesheet" href="https://fonts.googleapis.com/css2?family=Quicksand:wght@400;500;700&display=swap">
<style>
  :root {
    --emerald: #2eb892;
    --royal: #106fae;
    --card: #ffffff;
    --card-fade: #f6f7f7;
    --backdrop: #e4e6e8;
    --mist: #e9f2ef;
  }
  * { margin: 0; padding: 0; box-sizing: border-box; }
  html, body {
    width: 1200px; height: 800px; overflow: hidden;
    background: var(--backdrop);
    font-family: "Quicksand", sans-serif;
  }
  .canvas { position: relative; width: 1200px; height: 800px; }
  .card {
    position: absolute; left: 75px; top: 100px;
    width: 1050px; height: 600px;
    border-radius: 40px; overflow: hidden;
    background: linear-gradient(180deg, var(--card) 0%, var(--card-fade) 100%);
    box-shadow: 0 6px 18px rgba(0,0,0,.12);
  }
  .brand { position: absolute; left: 300px; top: 40px; width: 360px; height: 220px; }
  .brand-circle {
    position: absolute; left: 90px; top: 0; width: 220px; height: 220px;
    border-radius: 50%; background: var(--mist);
  }
  .brand-name {
    position: absolute; left: 0; top: 78px; width: 360px; text-align: center;
    font-weight: 500; font-size: 58px; letter-spacing: 1px; color: var(--emerald);
  }
  .identity { position: absolute; right: 55px; top: 196px; text-align: right; }
  .identity-name { font-weight: 700; font-size: 38px; letter-spacing: 1.5px; color: var(--emerald); }
  .identity-title { font-weight: 500; font-size: 24px; color: var(--royal); margin-top: 2px; }
  .divider { position: absolute; left: 0; right: 0; top: 312px; height: 3px; background: var(--emerald); }
  .contact {
    position: absolute; display: flex; align-items: center; gap: 20px;
    font-size: 30px; font-weight: 500; letter-spacing: 1.5px; color: var(--emerald);
  }
  .contact svg { width: 48px; height: 48px; flex: none; }
  .contact-phone { left: 165px; top: 365px; }
  .contact-web { left: 560px; top: 345px; }
  .contact-mail { left: 360px; top: 440px; }
  .band { position: absolute; left: 0; right: 0; bottom: 0; height: 62px; background: var(--royal); }
</style>
</head>
<body>
<div class="canvas">
  <div class="card">
    <div class="brand">
      <div class="brand-circle"></div>
      <div class="brand-name">Marlow Yoga</div>
    </div>

    <div class="identity">
      <div class="identity-name">Danielle Marlow</div>
      <div class="identity-title">Certified Yoga for Scoliosis Instructor</div>
    </div>

    <div class="divider"></div>

    <div class="contact contact-phone">
      <svg viewBox="0 0 48 48" aria-hidden="true">
        <polygon points="24,3 45,18 37,44 11,44 3,18" fill="var(--royal)"/>
        <path d="M18 15c2-1 3 0 4 2l1 3c0 1-1 2-2 2 1 3 3 5 6 6 0-1 1-2 2-2l3 1c2 1 3 2 2 4-1 2-3 3-5 2-6-2-10-6-12-12-1-2 0-5 1-6z" fill="#fff"/>
      </svg>
      <span>555-412-3097</span>
    </div>

    <div class="contact contact-web">
      <svg viewBox="0 0 48 48" aria-hidden="true">
        <polygon points="24,3 45,18 37,44 11,44 3,18" fill="var(--royal)"/>
        <rect x="12" y="15" width="24" height="16" rx="1.5" fill="none" stroke="#fff" stroke-width="2.5"/>
        <rect x="21" y="31" width="6" height="4" fill="#fff"/>
        <rect x="17" y="35" width="14" height="2.5" fill="#fff"/>
      </svg>
      <span>MarlowYoga.example</span>
    </div>

    <div class="contact contact-mail">
      <svg viewBox="0 0 48 48" aria-hidden="true">
        <polygon points="24,3 45,18 37,44 11,44 3,18" fill="var(--royal)"/>
        <rect x="12" y="17" width="24" height="16" fill="none" stroke="#fff" stroke-width="2.2"/>
        <polyline points="12,17 24,27 36,17" fill="none" stroke="#fff" stroke-width="2.2"/>
      </svg>
      <span>MarlowYoga@mailbox.example</span>
    </div>

    <div class="band"></div>
  </div>
</div>
</body>
</html>
```